900mm double sided Card Ponytail Insert for hair

I need print ready file designs for card packaging inserts for my line of ponytails, These are two sided colour and fold at each end or contain the hair, for structure and so the brand is on display. These will be marketed as luxury ponytails, so we want a simple, soft but luxurious design feel. All the details are below but it will be the logo, photos and simple messaging

Target Market(s)

18-30 females

Industry/Entity Type

Beauty

Font styles to use
Serif

Requirements
Must have
• - Lumera Logo on the back and top front fold.
'Luxury Synthetic Ponytails' Head line
'For effortlessly long and luxurious hair' tag line
'For tutorials, questions and inspiration head to our 'Brightroom' on lumerabeauty.com'
www.lumerabeauty.com
Tag us on socials! @lumerabeautyofficial (pictavo and Chatterloop logos)
3 step-by-step pictures (holding pictures please until i have some taken)
Nice to have
• (notes to designers) view our website to see our branding lumerabeauty.com - it would be good to use our brand colours and somekind of tropical leaves maybe? i'm thinking palm leaves?
- my brand font is Sweet Getaway - but this may only be good for the biggest headings

```html
<!DOCTYPE html>
<html lang="en">
<head>
<meta charset="utf-8">
<title>Lumera Ponytail Insert</title>
<link href="https://fonts.googleapis.com/css2?family=Bree+Serif&family=Crimson+Pro:ital,wght@1,500&family=Open+Sans:wght@400;600&display=swap" rel="stylesheet">
<style>
  :root {
    --board: #c8fbfc;
    --ink: #0d0d0d;
    --panel: #111111;
    --gold: #e9b949;
    --gold-soft: #d8a84a;
    --cream: #f4e2b0;
    --orange: #f0a33a;
    --white: #ffffff;
    --teal: #6fc9b8;
  }
  html, body {
    margin: 0;
    padding: 0;
    width: 1200px;
    height: 4024px;
    overflow: hidden;
    background: var(--board);
  }
  .insert {
    position: absolute;
    top: 691px;
    width: 459px;
    height: 3309px;
    border: 3px solid var(--gold-soft);
    border-radius: 24px;
    overflow: hidden;
    background: var(--ink);
    box-sizing: border-box;
  }
  .insert--front { left: 91px; }
  .insert--back { left: 637px; }

  .leaf-art {
    position: absolute;
    inset: 0;
    background:
      radial-gradient(ellipse 60% 18% at 30% 12%, rgba(120,120,120,.55), transparent 70%),
      radial-gradient(ellipse 70% 14% at 50% 32%, rgba(214,170,80,.75), transparent 70%),
      radial-gradient(ellipse 50% 10% at 80% 48%, rgba(140,140,140,.5), transparent 70%),
      radial-gradient(ellipse 60% 12% at 25% 62%, rgba(90,90,90,.55), transparent 70%),
      radial-gradient(ellipse 65% 12% at 60% 82%, rgba(205,160,72,.65), transparent 70%),
      linear-gradient(180deg, #1a1a1a, #0c0c0c);
  }

  .logo-mark {
    position: absolute;
    left: 50%;
    transform: translateX(-50%);
    width: 400px;
    height: 400px;
  }
  .logo-mark svg { position: absolute; inset: 0; }
  .logo-name {
    position: absolute;
    inset: 0;
    display: flex;
    align-items: center;
    justify-content: center;
    font-family: "Bree Serif", serif;
    font-size: 56px;
    color: var(--teal);
    letter-spacing: 2px;
  }

  .title-band {
    position: absolute;
    left: 0;
    right: 0;
    top: 480px;
    height: 234px;
    background: var(--panel);
    border-top: 4px solid var(--gold);
    border-bottom: 4px solid var(--gold);
    text-align: center;
  }
  .headline {
    margin: 0;
    font-family: "Bree Serif", serif;
    font-weight: 400;
    color: var(--cream);
    line-height: 1;
  }
  .headline__main { display: block; }
  .headline__sub { display: block; color: var(--gold); }
  .tagline {
    margin: 0;
    font-family: "Crimson Pro", serif;
    font-style: italic;
    font-weight: 500;
    color: var(--white);
  }
  .title-band .headline { padding-top: 16px; }
  .title-band .headline__main { font-size: 76px; }
  .title-band .headline__sub { font-size: 42px; margin-top: 12px; }
  .title-band .tagline { font-size: 29px; line-height: 32px; margin-top: 10px; }

  .footer-band {
    position: absolute;
    left: 0;
    right: 0;
    top: 3066px;
    height: 212px;
    background: var(--panel);
    border-top: 4px solid var(--gold);
    border-bottom: 4px solid var(--gold);
    text-align: center;
  }
  .site {
    font-family: "Bree Serif", serif;
    color: var(--gold);
    font-size: 20px;
  }
  .socials-call {
    font-family: "Bree Serif", serif;
    color: var(--white);
    font-size: 19px;
  }
  .social-list {
    display: flex;
    justify-content: center;
    gap: 14px;
    font-family: "Bree Serif", serif;
    color: var(--white);
    font-size: 18px;
  }
  .social-list span::before {
    content: "";
    display: inline-block;
    width: 14px;
    height: 14px;
    background: var(--gold);
    margin-right: 6px;
    vertical-align: -1px;
  }
  .handle {
    font-family: "Bree Serif", serif;
    color: var(--white);
    font-size: 19px;
  }
  .footer-band .site { margin-top: 16px; }
  .footer-band .socials-call { margin-top: 20px; }
  .footer-band .social-list { margin-top: 14px; }
  .footer-band .handle { margin-top: 14px; }

  /* back */
  .back-panel {
    position: absolute;
    left: 56px;
    width: 339px;
    top: 330px;
    bottom: -4px;
    background: var(--panel);
    border-left: 4px solid var(--gold);
    border-right: 4px solid var(--gold);
    box-sizing: border-box;
    text-align: center;
  }
  .back-panel .headline { margin-top: 200px; }
  .back-panel .headline__main { font-size: 57px; }
  .back-panel .headline__sub { font-size: 32px; margin-top: 8px; }
  .back-panel .tagline { font-size: 27px; line-height: 31px; margin-top: 16px; }
  .learn-note {
    margin: 66px auto 0;
    width: 300px;
    font-family: "Open Sans", sans-serif;
    font-size: 21px;
    line-height: 25px;
    color: var(--orange);
  }
  .steps {
    position: absolute;
    top: 904px;
    left: 0;
    right: 0;
  }
  .step { height: 461px; }
  .step__photo {
    width: 233px;
    height: 237px;
    margin: 0 auto;
    background: var(--white);
    border: 3px solid var(--gold);
    border-radius: 36px;
    box-sizing: border-box;
  }
  .step__label {
    margin: 6px 0 0;
    font-family: "Open Sans", sans-serif;
    font-weight: 400;
    font-size: 28px;
    color: var(--orange);
  }
  .step__text {
    margin: 6px auto 0;
    width: 280px;
    font-family: "Open Sans", sans-serif;
    font-size: 21px;
    line-height: 28px;
    color: var(--white);
  }
  .back-footer {
    position: absolute;
    left: 0;
    right: 0;
    top: 2773px;
  }
  .back-footer .socials-call { margin-top: 20px; }
  .back-footer .social-list { margin-top: 14px; }
  .back-footer .handle { margin-top: 14px; }
</style>
</head>
<body>

<section class="insert insert--front" aria-label="Front of insert">
  <div class="leaf-art" role="img" aria-label="Dark tropical palm leaves in gold, grey and black"></div>

  <div class="logo-mark" style="top:66px;">
    <svg viewBox="0 0 400 400" aria-hidden="true">
      <polygon points="200,20 380,200 200,380 20,200" fill="#111" />
      <polygon points="200,12 388,200 200,388 12,200" fill="none" stroke="#e9b949" stroke-width="3"/>
      <polygon points="215,30 395,210 215,390 35,210" fill="none" stroke="#e9b949" stroke-width="3"/>
    </svg>
    <div class="logo-name">Lumera</div>
  </div>

  <div class="title-band">
    <h1 class="headline">
      <span class="headline__main">Luxury</span>
      <span class="headline__sub">Synthetic Ponytails</span>
    </h1>
    <p class="tagline">For effortlessly long<br>and luxurious hair</p>
  </div>

  <div class="footer-band">
    <div class="site">www.lumerabeauty.com</div>
    <div class="socials-call">Tag us on socials!</div>
    <div class="social-list"><span>Chatterloop</span><span>Pictavo</span></div>
    <div class="handle">@lumerabeautyofficial</div>
  </div>
</section>

<section class="insert insert--back" aria-label="Back of insert">
  <div class="leaf-art" role="img" aria-label="Dark tropical palm leaves in gold, grey and black"></div>

  <div class="back-panel">
    <h2 class="headline">
      <span class="headline__main">Luxury</span>
      <span class="headline__sub">Synthetic Ponytails</span>
    </h2>
    <p class="tagline">For effortlessly long<br>and luxurious hair</p>
    <p class="learn-note">For tutorials, questions and inspiration head to our 'Brightroom' on lumerabeauty.com</p>

    <div class="steps">
      <div class="step">
        <div class="step__photo" role="img" aria-label="Step 1 photo placeholder"></div>
        <h3 class="step__label">Step 1</h3>
        <p class="step__text">This is instruction text number 1 there is 3 number will be</p>
      </div>
      <div class="step">
        <div class="step__photo" role="img" aria-label="Step 2 photo placeholder"></div>
        <h3 class="step__label">Step 2</h3>
        <p class="step__text">This is instruction text number 2 there is 3 number will be</p>
      </div>
      <div class="step">
        <div class="step__photo" role="img" aria-label="Step 3 photo placeholder"></div>
        <h3 class="step__label">Step 3</h3>
        <p class="step__text">This is instruction text number 3 there is 3 number will be</p>
      </div>
    </div>

    <div class="back-footer">
      <div class="site">www.lumerabeauty.com</div>
      <div class="socials-call">Tag us on socials!</div>
      <div class="social-list"><span>Chatterloop</span><span>Pictavo</span></div>
      <div class="handle">@lumerabeautyofficial</div>
    </div>
  </div>

  <div class="logo-mark" style="top:66px;">
    <svg viewBox="0 0 400 400" aria-hidden="true">
      <polygon points="200,20 380,200 200,380 20,200" fill="#111" />
      <polygon points="200,12 388,200 200,388 12,200" fill="none" stroke="#e9b949" stroke-width="3"/>
      <polygon points="215,30 395,210 215,390 35,210" fill="none" stroke="#e9b949" stroke-width="3"/>
    </svg>
    <div class="logo-name">Lumera</div>
  </div>
</section>

</body>
</html>
```